Small consulting business needs logo and business card design

I need a logo, business card and letterhead design for a small consulting firm called Veltramo Consulting. My customers are generally small to medium sized businesses but I have done work for major corporates and government departments. The field of consulting is strategic/business planning and program management. I have blue as the predominate colour in my current business card but I am happy to change this for the right design
Industry/Entity Type
Business

```html
<!DOCTYPE html>
<html lang="en">
<head>
<meta charset="utf-8">
<title>Veltramo Consulting – Business Card</title>
<link rel="stylesheet" href="https://fonts.googleapis.com/css2?family=Arimo:wght@400;700&display=swap">
<style>
  :root {
    --backdrop: #e9e7e3;
    --card: #f6f6f6;
    --ink: #262626;
    --lavender: #b4c6e8;
    --lavender-soft: #d3def2;
    --teal: #93d3dc;
    --teal-light: #b3e0e6;
    --teal-deep: #80c9d3;
  }
  * { box-sizing: border-box; margin: 0; padding: 0; }
  html, body {
    width: 1200px;
    height: 804px;
    overflow: hidden;
    background: var(--backdrop);
    font-family: "Arimo", Arial, sans-serif;
    color: var(--ink);
  }
  .business-card {
    position: absolute;
    left: 150px;
    top: 145px;
    width: 900px;
    height: 514px;
    background: var(--card);
    box-shadow: 0 6px 24px rgba(0,0,0,.12);
    overflow: hidden;
  }
  .block { position: absolute; }
  .block--lavender { left: 216px; top: 0; width: 190px; height: 140px; background: var(--lavender); }
  .block--teal { left: 350px; top: 0; width: 316px; height: 258px; background: var(--teal); }
  .block--teal-light { left: 576px; top: 0; width: 324px; height: 128px; background: var(--teal-light); }
  .block--overlap { left: 576px; top: 0; width: 90px; height: 128px; background: var(--teal-deep); }

  .contact { position: absolute; left: 0; top: 0; width: 100%; height: 100%; }
  .contact__name {
    position: absolute; left: 80px; top: 188px;
    font-size: 38px; font-weight: 700; letter-spacing: .5px;
  }
  .contact__line { position: absolute; font-size: 21px; white-space: nowrap; }
  .contact__phone { left: 104px; top: 244px; }
  .contact__address { left: 150px; top: 300px; font-size: 19px; }
  .email-band {
    position: absolute; left: 0; top: 400px;
    width: 500px; height: 56px; background: var(--lavender-soft);
  }
  .contact__email { left: 104px; top: 416px; font-size: 22px; }

  .brand {
    position: absolute; left: 590px; top: 272px;
    display: flex; align-items: center; gap: 14px;
  }
  .brand__mark { width: 18px; height: 18px; background: var(--ink); }
  .brand__name {
    font-size: 30px; font-weight: 700; line-height: 1.05;
    letter-spacing: 1px; text-transform: uppercase; color: var(--ink);
  }
</style>
</head>
<body>
  <article class="business-card">
    <div class="block block--lavender"></div>
    <div class="block block--teal"></div>
    <div class="block block--teal-light"></div>
    <div class="block block--overlap"></div>

    <div class="brand">
      <span class="brand__mark"></span>
      <span class="brand__name">Veltramo<br>Consulting</span>
    </div>

    <div class="contact">
      <h1 class="contact__name">Your Name</h1>
      <p class="contact__line contact__phone">M:0400 318 275</p>
      <p class="contact__line contact__address">A: Street Address</p>
      <div class="email-band"></div>
      <p class="contact__line contact__email">E: abc@velmail.com</p>
    </div>
  </article>
</body>
</html>
```